Corvel Lighting needs a new website (only informative)

Corvel Lighting (Pty) Ltd imports and distributes LED lighting products to South Africa. Our existing website (www.corvel-example.co.za) is designed and implemented on a shopping cart template: Trovi-Basket.

The website needs to be redesigned. It should no longer be based on a shopping cart template, but purely informative and allow some PDF downloads. It should scale well and allow quick & easy changes by the website owner: Including adding, changing and removing products. Other information pages should also be easy to manage.

No need to design a logo. A logo and user requirement specification is uploaded with more details.

Target Market(s)

Retailers, interior designers, architects, contractors, electricians, franchises etc. with a need for energy efficient LED lighting.

Industry/Entity Type

Shopping

Font styles to use
Sans Serif

Colors
0355a3
0892cd
86cae6
86cfc6

Requirements
Must have
• Existing logo to be used.
All pages informative & PDF download capability.
User friendly management
SEO capability

```html
<!DOCTYPE html>
<html lang="en">
<head>
<meta charset="utf-8">
<title>Corvel Lighting</title>
<link rel="stylesheet" href="https://fonts.googleapis.com/css2?family=Mulish:wght@300;400;600;700;800&family=Questrial&display=swap">
<style>
:root{
  --brand:#1a5d7e;
  --brand-bright:#0892cd;
  --ink:#222;
  --muted:#9a9a9a;
  --line:#d8d8d8;
  --band:#f3f3f3;
  --dark:#3b3b3b;
  --footer:#3a3a3a;
  --footer-text:#d6d6d6;
  --button-gray:#b7b7b7;
}
*{box-sizing:border-box;margin:0;padding:0}
html,body{width:882px;height:1200px;overflow:hidden;background:#fff}
body{position:relative;font-family:"Mulish",sans-serif;color:var(--ink)}
.abs{position:absolute}

/* header */
.brand{left:74px;top:34px;display:flex;align-items:center;gap:8px}
.brand-mark{width:14px;height:14px;background:var(--brand);border-radius:50%}
.brand-name{font-family:"Questrial",sans-serif;font-size:28px;color:var(--brand);letter-spacing:.5px}
.pdf-btn{left:476px;top:45px;width:79px;height:28px;background:var(--button-gray);font-family:"Questrial",sans-serif;font-size:11px;color:#222;display:flex;align-items:center;justify-content:center}
.social{left:576px;top:53px;display:flex;gap:12px}
.social span{width:14px;height:14px;border-radius:50%;background:#555;display:block}
.top-divider{left:684px;top:52px;width:1px;height:16px;background:#ccc}
.top-links{left:696px;top:54px;font-size:9px;color:var(--muted);display:flex;gap:12px}

/* nav */
.main-nav{left:74px;top:105px;width:734px;height:33px;border:1px solid var(--line);display:flex;align-items:center}
.main-nav .home{width:22px;display:flex;justify-content:center}
.main-nav a{font-family:"Questrial",sans-serif;font-size:10px;color:#111;text-decoration:none;padding:0 14px;border-right:1px solid var(--line);line-height:18px}
.main-nav a:last-of-type{border-right:none}
.search-btn{position:absolute;right:-1px;top:-1px;width:26px;height:33px;background:var(--brand);display:flex;align-items:center;justify-content:center}

/* slider */
.slider{left:74px;top:154px;width:724px;height:301px;border:1px solid #aaa;background:#fff;padding:5px}
.slider-inner{width:100%;height:100%;border:1px solid #ccc;position:relative;background:linear-gradient(90deg,#fff 75%,#f4f4f4 100%)}
.slide-photo{position:absolute;left:30px;top:20px;width:430px;height:250px;background:radial-gradient(ellipse at 40% 50%,#dcdcdc 0%,#a8a8a8 40%,#e8e8e8 75%,#fff 100%)}
.slide-title{left:501px;top:76px;font-size:22px;font-weight:800;letter-spacing:.5px;color:#111}
.slide-sub{left:501px;top:110px;font-size:11px;font-weight:600;color:#111}
.slide-text{left:501px;top:130px;width:200px;font-size:8.5px;line-height:14.5px;text-transform:uppercase;color:#222}
.outline-btn{width:76px;height:32px;border:1px solid #ccc;background:#fff;font-family:"Questrial",sans-serif;font-size:11px;display:flex;align-items:center;justify-content:center;color:#111}
.slide-btn{left:503px;top:200px}
.slide-arrows{left:506px;top:251px;display:flex;gap:12px}
.slide-arrows span{width:17px;height:20px;background:#bdbdbd;display:flex;align-items:center;justify-content:center}

/* products */
.product-band{left:0;top:470px;width:882px;height:242px;background:var(--band)}
.product{width:203px}
.product.featured{background:#fff;border:1px solid var(--line)}
.product h3{font-family:"Questrial",sans-serif;font-weight:400;font-size:19px;color:#222;display:flex;align-items:center;gap:8px;padding-bottom:8px;border-bottom:1px solid var(--line);width:162px}
.bulb{width:10px;height:16px;background:#ddd;border-radius:5px 5px 2px 2px}
.product-photo{width:80px;height:70px;margin:10px 0 0 38px;background:radial-gradient(circle,#d0d0d0,#f2f2f2);border-radius:8px}
.product p{width:175px;margin-top:10px;font-family:"Questrial",sans-serif;font-size:8.5px;line-height:14.7px;text-align:justify;text-align-last:justify}
.dark-btn{width:50px;height:25px;background:var(--dark);color:#fff;font-size:10px;font-weight:600;border-radius:2px;display:flex;align-items:center;justify-content:center;margin-top:10px;box-shadow:1px 1px 2px rgba(0,0,0,.3)}

.section-rule{left:70px;top:768px;width:740px;height:4px;background:radial-gradient(ellipse at center,#d5d5d5 0%,rgba(255,255,255,0) 70%)}

/* info blocks */
.info-title{font-size:17px;font-weight:800;color:#222}
.info-title em{font-style:normal;color:var(--brand)}
.info-sub{font-size:10px;color:var(--muted);padding-bottom:5px;border-bottom:1px solid #ccc;margin-top:6px}
.about{left:73px;top:793px}
.about .info-sub{width:257px}
.about-text{left:73px;top:845px;width:465px;font-family:Arial,sans-serif;font-size:9px;line-height:16px;color:#444}
.about-text p+p{margin-top:16px}
.about-btn{left:73px;top:983px}
.adv{left:597px;top:793px}
.adv .info-sub{width:130px}
.adv-text{left:600px;top:845px;width:175px;font-family:"Questrial",sans-serif;font-size:8.5px;line-height:13px;text-align:justify;text-align-last:justify}
.adv-list{left:600px;top:880px;width:202px;list-style:none}
.adv-list li{height:30px;background:#f0f0f0;border-bottom:1px solid #fff;display:flex;align-items:center;gap:10px;padding-left:3px;font-family:"Questrial",sans-serif;font-size:10px}
.tick{width:12px;height:12px;border-radius:50%;background:var(--brand);display:flex;align-items:center;justify-content:center}
.adv-btn{left:602px;top:983px}

/* footer */
.site-footer{left:0;top:1040px;width:882px;height:160px;background:var(--footer);color:var(--footer-text)}
.f-col{position:absolute;top:18px}
.f-col h4{font-size:11px;font-weight:700;color:#fff}
.f-col h4.big{font-family:"Questrial",sans-serif;font-weight:400;font-size:15px}
.f-contact{left:75px;font-size:10px;line-height:15.5px}
.f-contact address{font-style:normal;margin-top:14px}
.f-links{left:281px}
.f-links ul{list-style:none;margin-top:10px;font-size:7.5px;line-height:14.7px;color:#fff;padding-left:3px}
.f-blog{left:491px}
.f-blog a{display:block;margin-top:12px;font-size:8px;font-weight:700;color:#fff;text-decoration:underline}
.f-blog p{margin-top:12px;font-size:7.5px;line-height:10.5px;width:150px}
.f-sep{position:absolute;top:24px;width:1px;height:100px;background:#555}
.f-brand{left:662px;top:30px;display:flex;align-items:center;gap:6px}
.f-brand .brand-mark{background:#bbb;width:10px;height:10px}
.f-brand span{font-family:"Questrial",sans-serif;font-size:20px;color:#cfcfcf}
.f-social{left:700px;top:88px;display:flex;gap:6px}
.f-social span{width:21px;height:21px;border-radius:50%;border:1px solid #ccc;background:#777;display:block}
.f-rule{left:75px;top:130px;width:735px;height:1px;background:#555}
.copyright{left:78px;top:140px;font-size:8px;font-weight:600;color:#fff}
</style>
</head>
<body>

<header>
  <div class="abs brand"><span class="brand-mark"></span><span class="brand-name">Corvel Lighting</span></div>
  <div class="abs pdf-btn">Download PDF</div>
  <div class="abs social"><span></span><span></span><span></span><span></span></div>
  <div class="abs top-divider"></div>
  <div class="abs top-links"><span>Documentation</span><span>Support</span></div>
</header>

<nav class="abs main-nav">
  <span class="home"><svg width="10" height="10" viewBox="0 0 10 10"><path d="M5 0L0 5h1.5v5h2.5V7h2v3h2.5V5H10z" fill="#1a5d7e"/></svg></span>
  <a>LED down lights</a><a>LED bulbs</a><a>LED tube lights</a><a>Dimmable LED lamps</a><a>Flood Lights</a><a>LED strip lights</a><a>Other LED lights</a>
  <span class="search-btn"><svg width="13" height="13" viewBox="0 0 13 13"><circle cx="5" cy="5" r="3.5" stroke="#fff" stroke-width="1.8" fill="none"/><path d="M7.5 7.5L12 12" stroke="#fff" stroke-width="2"/></svg></span>
</nav>

<section class="abs slider">
  <div class="slider-inner">
    <div class="slide-photo" role="img" aria-label="Chrome LED lamp housing with black cable"></div>
    <h1 class="abs slide-title">MASTERPIECE</h1>
    <h2 class="abs slide-sub">IN BUSINESS DEVELOPMENT</h2>
    <p class="abs slide-text">Lorem ipsum dolor sit amet, consectetur adipisicing elit, sed do eiusmod tempor incididunt uted labore et dolore magna aliqua.</p>
    <div class="abs outline-btn slide-btn">Read More</div>
    <div class="abs slide-arrows">
      <span><svg width="8" height="12"><path d="M7 1L2 6l5 5" stroke="#fff" stroke-width="1.5" fill="none"/></svg></span>
      <span><svg width="8" height="12"><path d="M1 1l5 5-5 5" stroke="#fff" stroke-width="1.5" fill="none"/></svg></span>
    </div>
  </div>
</section>

<div class="abs product-band"></div>
<article class="abs product" style="left:73px;top:490px">
  <h3><span class="bulb"></span>LED down lights</h3>
  <div class="product-photo" role="img" aria-label="LED spot bulb"></div>
  <p>Casaesaert viasead setertya aseteciega nveritide nerafae kertyeritaesa ertyatya aplicaboserde miuas oditaut. onequuntures magni dolores eonemo enipta volupta equi nesciunt ades. Nernatur aut qui ratione</p>
  <div class="dark-btn">More</div>
</article>
<article class="abs product featured" style="left:330px;top:489px;height:245px;padding:6px 0 0 10px">
  <h3><span class="bulb"></span>LED down lights</h3>
  <div class="product-photo" role="img" aria-label="LED reflector lamp"></div>
  <p>Casaesaert viasead setertya aseteciega nveritide nerafae kertyeritaesa ertyatya aplicaboserde miuas oditaut. onequuntures magni dolores eonemo enipta volupta equi nesciunt ades. Nernatur aut qui ratione</p>
  <div class="dark-btn">More</div>
</article>
<article class="abs product" style="left:628px;top:490px">
  <h3><span class="bulb"></span>LED down lights</h3>
  <div class="product-photo" role="img" aria-label="LED flood light"></div>
  <p>Casaesaert viasead setertya aseteciega nveritide nerafae kertyeritaesa ertyatya aplicaboserde miuas oditaut. onequuntures magni dolores eonemo enipta volupta equi nesciunt ades. Nernatur aut qui ratione</p>
  <div class="dark-btn">More</div>
</article>

<div class="abs section-rule"></div>

<section class="abs about">
  <h2 class="info-title">What <em>We Do</em></h2>
  <div class="info-sub">Mauris eget diam nibh, at sollicitudin nunc</div>
</section>
<div class="abs about-text">
  <p>Lorem Ipsum is simply dummy text of the printing and typesetting industry. Lorem Ipsum has been the industry's standard dummy text ever since the 1500s, when an unknown printer took a galley of type and scrambled it to make a type specimen book. It has survived not only five centuries,</p>
  <p>&nbsp;but also the leap into electronic typesetting, remaining essentially unchanged. It was popularised in the 1960s with the release of transfer lettering sheets containing Lorem Ipsum passages, and more recently with desktop publishing and layout programs including versions of Lorem Ipsum.</p>
</div>
<div class="abs outline-btn about-btn">Read More</div>

<section class="abs adv">
  <h2 class="info-title">Our <em>advantages</em></h2>
  <div class="info-sub">healthy lifestyle</div>
</section>
<p class="abs adv-text">Casaesaert viasead setertya aseteciega nveritide nerafae kertyeritaesa ertyatya apli</p>
<ul class="abs adv-list">
  <li><span class="tick"><svg width="6" height="6"><path d="M1.5 0.5l3 2.5-3 2.5" stroke="#fff" fill="none"/></svg></span>Casaesaert viasead setertya asete</li>
  <li><span class="tick"><svg width="6" height="6"><path d="M1.5 0.5l3 2.5-3 2.5" stroke="#fff" fill="none"/></svg></span>Casaesaert viasead setertya asete</li>
  <li><span class="tick"><svg width="6" height="6"><path d="M1.5 0.5l3 2.5-3 2.5" stroke="#fff" fill="none"/></svg></span>Casaesaert viasead setertya asete</li>
</ul>
<div class="abs outline-btn adv-btn">Read More</div>

<footer class="abs site-footer">
  <div class="f-col f-contact">
    <h4>Contact Us</h4>
    <address>TEL: 000-200-3001<br>Fax: 000-200-3002<br>88 Harbour Lane Suite 204<br>Port Ellis, WC 7400</address>
  </div>
  <div class="f-sep" style="left:266px"></div>
  <div class="f-col f-links">
    <h4 class="big">Quick links</h4>
    <ul><li>Home</li><li>About Us</li><li>Products</li><li>Contact Us</li></ul>
  </div>
  <div class="f-sep" style="left:465px"></div>
  <div class="f-col f-blog">
    <h4>Blog</h4>
    <a>Lorem ipsum dolor sit amet</a>
    <p>Lorem ipsum dolor sit amet, consectetuer adipiscing elit, sed diam nonummy nibh euismod tincidunt ut laoreet dolore magna</p>
  </div>
  <div class="f-sep" style="left:655px"></div>
  <div class="abs f-brand"><span class="brand-mark"></span><span>Corvel Lighting</span></div>
  <div class="abs f-social"><span></span><span></span><span></span></div>
  <div class="abs f-rule"></div>
  <div class="abs copyright">Copyright 2012 Pellimore Studio | Web Design &amp; Web Development by Quillstead Web Works</div>
</footer>

</body>
</html>
```